Korvane - Business Card Design

Design a modern masculine business card for our business

Target Market(s)

Private Market

Industry/Entity Type

Construction

Contact Information for Business Card

Company Name - Name of Person - Address - email address - contact number

Font styles to use
Serif
Sans Serif

Colors
0094D4
00A9DD
6FCCEA
C7EBF8
E9F6FB
00AB8E
00BBA5
67D7C9
C6EFE9
E9F9F6
F0912C
F2A743
F7CA91
FBE8D2
FDF5EE

Requirements
Must have
• Use company logo provided
Nice to have
• Company Logo

```html
<!DOCTYPE html>
<html lang="en">
<head>
<meta charset="utf-8">
<title>Korvane – Business Card</title>
<link href="https://fonts.googleapis.com/css2?family=Montserrat:wght@400;500;700;800&display=swap" rel="stylesheet">
<style>
  :root {
    --bg: #e9e9e9;
    --card: #f3f1f0;
    --charcoal: #3a3a3a;
    --orange: #ee7f3d;
    --light-grey: #dcdcdc;
    --text: #555555;
  }
  * { margin: 0; padding: 0; box-sizing: border-box; }
  html, body {
    width: 1200px; height: 853px; overflow: hidden;
    background: var(--bg);
    font-family: "Montserrat", sans-serif;
  }
  .stage {
    width: 1200px; height: 853px;
    display: flex; align-items: center; justify-content: center; gap: 40px;
  }
  .card {
    position: relative;
    width: 540px; height: 309px;
    background: var(--card);
    border-radius: 22px;
    overflow: hidden;
    box-shadow: 0 6px 18px rgba(0,0,0,0.10);
  }
  .card-art { position: absolute; inset: 0; }
  .wordmark {
    position: absolute;
    display: flex; align-items: center; gap: 8px;
    font-weight: 800; color: var(--charcoal);
    letter-spacing: 0.04em; text-transform: uppercase;
    white-space: nowrap;
  }
  .wordmark-square { width: 12px; height: 12px; background: var(--orange); }
  .card-back .wordmark { left: 50%; top: 50%; transform: translate(-50%, -50%); font-size: 36px; }
  .card-front .wordmark { left: 36px; top: 36px; font-size: 28px; }
  .contact-block {
    position: absolute; right: 26px; top: 112px;
    text-align: right; color: var(--text);
  }
  .person-name { font-size: 17px; font-weight: 700; color: var(--charcoal); }
  .person-name .accent { color: var(--orange); }
  .person-role { font-size: 10px; margin-top: 2px; }
  .contact-list { list-style: none; margin-top: 18px; font-size: 10px; line-height: 1.55; }
  .contact-list li { display: flex; justify-content: flex-end; align-items: center; gap: 8px; }
  .contact-list svg { width: 10px; height: 10px; fill: var(--orange); flex: none; }
  .row-name { display: flex; justify-content: flex-end; align-items: center; gap: 8px; }
  .row-name svg { width: 11px; height: 11px; fill: var(--orange); }
</style>
</head>
<body>
<main class="stage">

  <section class="card card-back" aria-label="Card back">
    <svg class="card-art" viewBox="0 0 540 309" aria-hidden="true">
      <rect class="band-upper" x="0" y="96" width="170" height="10" fill="var(--orange)"/>
      <rect class="band-upper-dot" x="178" y="96" width="10" height="10" fill="var(--charcoal)"/>
      <rect class="band-lower-dot" x="352" y="203" width="10" height="10" fill="var(--charcoal)"/>
      <rect class="band-lower" x="370" y="203" width="170" height="10" fill="var(--orange)"/>
    </svg>
    <div class="wordmark"><span class="wordmark-square"></span>Korvane</div>
  </section>

  <section class="card card-front" aria-label="Card front">
    <svg class="card-art" viewBox="0 0 540 309" aria-hidden="true">
      <rect class="dark-panel" x="0" y="150" width="260" height="159" fill="var(--charcoal)"/>
      <rect class="dark-panel-low" x="260" y="220" width="110" height="89" fill="var(--charcoal)"/>
      <rect class="accent-band" x="0" y="176" width="230" height="14" fill="var(--orange)"/>
      <rect class="accent-tick" x="240" y="176" width="14" height="14" fill="var(--card)"/>
      <rect class="corner-line" x="380" y="220" width="4" height="89" fill="var(--light-grey)"/>
    </svg>
    <div class="wordmark"><span class="wordmark-square"></span>Korvane</div>
    <div class="contact-block">
      <div class="row-name">
        <div>
          <p class="person-name">Name Of <span class="accent">Person</span></p>
          <p class="person-role">General Manager</p>
        </div>
        <svg viewBox="0 0 10 10"><circle cx="5" cy="3" r="2.4"/><path d="M0.5 10 Q5 3.8 9.5 10Z"/></svg>
      </div>
      <ul class="contact-list">
        <li>+000 123 456 7890
          <svg viewBox="0 0 10 10"><path d="M2 0.5 L3.8 3 L2.8 4 Q4 6.5 6 7.2 L7 6.2 L9.5 8 L8.3 9.5 Q2 8.5 0.5 1.7Z"/></svg></li>
        <li>yourmail@korvanemail.com
          <svg viewBox="0 0 10 10"><rect x="0.5" y="2" width="9" height="6.5"/><path d="M0.5 2 L5 5.8 L9.5 2" stroke="var(--card)" stroke-width="0.9" fill="none"/></svg></li>
        <li>your street name here<br>New York City, Zip - 000
          <svg viewBox="0 0 10 10"><path d="M5 10 L1.6 5 A3.8 3.8 0 1 1 8.4 5Z"/><circle cx="5" cy="3.6" r="1.3" fill="var(--card)"/></svg></li>
      </ul>
    </div>
  </section>

</main>
</body>
</html>
```